December online webinar for our coaching and mentoring business.

needing an email flyer and something to use on appropriate social media e.g. Instagram to promote our December half day webinar focusing on positive mindset, relationships and 2021 being a new year with new opportunities. For the feel of what we have done previously:
www.qlvgetaways.com.au
We will be using 2 guest speakers:
Marcus Elwood of BucketGoals.com and
Lorena Voss, psychologist and both will need to be prominent on the marketing material we send out on email and use on social media.
The webinar will likely run Thursday December 10th from 12.30pm to 4.30pm AEST and will be hosted and facilitated by me and on behalf of Tarrow Business Coaching.
I am thinking colour schemes and branding similar to what you see on the website above.
Pricing needs to be on the flyer - $750 + GST per person*
*enquire for multi booking discounts for 2 people or more

Target Market(s)

people looking for a boost before the year end and a fast start to 2021

Font styles to use
Sans Serif

Requirements
Must have
• see brief above
Nice to have
• see brief above
Should not have
• see brief above

```html
<!DOCTYPE html>
<html lang="en">
<head>
<meta charset="utf-8">
<title>December Webinar – Tarrow Business Coaching</title>
<link rel="stylesheet" href="https://fonts.googleapis.com/css2?family=Poppins:wght@300;400;600;700&display=swap">
<style>
  :root {
    --brand-red: #f1403a;
    --shape-red: #d8333a;
    --white: #ffffff;
    --ink: #1a1a1a;
    --yellow: #f1e637;
    --photo-pale: #e9e6dc;
    --photo-blue: #1f6f96;
    --photo-grey: #4a4f55;
  }
  * { margin: 0; padding: 0; box-sizing: border-box; }
  html, body { width: 686px; height: 1200px; overflow: hidden; }
  body {
    font-family: "Poppins", sans-serif;
    color: var(--white);
    background: var(--brand-red);
  }
  .flyer {
    position: relative;
    width: 686px;
    height: 1200px;
    background: var(--brand-red);
    overflow: hidden;
  }
  .graphics { position: absolute; inset: 0; }
  .accent { fill: var(--shape-red); }

  .kicker {
    position: absolute; left: 92px; top: 70px;
    font-size: 20.5px; font-weight: 300; letter-spacing: 0.2px;
  }
  .headline {
    position: absolute; left: 90px; top: 98px;
    font-size: 53px; font-weight: 600; line-height: 69px; letter-spacing: -0.3px;
  }
  .subhead {
    position: absolute; left: 91px; top: 243px;
    font-size: 32px; font-weight: 400; line-height: 47px;
  }

  .speaker { position: absolute; }
  .speaker-name { font-size: 30px; line-height: 34px; font-weight: 300; white-space: nowrap; }
  .speaker-name strong { font-weight: 700; }
  .speaker-role { font-size: 18px; font-weight: 400; color: var(--ink); line-height: 22px; }
  .speaker--psych { left: 91px; top: 424px; text-align: right; width: 198px; }
  .speaker--psych .speaker-name { text-align: left; }
  .speaker--goals { left: 388px; top: 748px; }

  .event-when {
    position: absolute; left: 55px; top: 855px;
    font-size: 30px; line-height: 35.5px; font-weight: 300;
  }
  .event-when strong { font-weight: 700; letter-spacing: -0.4px; }
  .pricing {
    position: absolute; left: 55px; top: 974px;
    font-size: 15.5px; font-weight: 300;
  }
  .pricing small { display: block; font-size: 11px; line-height: 15px; }

  .brand {
    position: absolute; left: 0; right: 0; top: 1090px;
    text-align: center;
    font-size: 22px; font-weight: 600; letter-spacing: 0.2px;
  }
</style>
</head>
<body>
<main class="flyer">
  <svg class="graphics" width="686" height="1200" viewBox="0 0 686 1200" aria-hidden="false">
    <defs>
      <linearGradient id="psych-photo" x1="0" y1="0" x2="0" y2="1">
        <stop offset="0" stop-color="var(--photo-pale)"/>
        <stop offset="0.45" stop-color="#d8c98a"/>
        <stop offset="0.55" stop-color="var(--photo-blue)"/>
        <stop offset="1" stop-color="#174f6e"/>
      </linearGradient>
      <linearGradient id="goals-photo" x1="0" y1="0" x2="0" y2="1">
        <stop offset="0" stop-color="var(--yellow)"/>
        <stop offset="0.35" stop-color="#e6d24a"/>
        <stop offset="0.5" stop-color="var(--photo-grey)"/>
        <stop offset="1" stop-color="#3a3e44"/>
      </linearGradient>
    </defs>

    <polygon class="accent" points="554,414 613,389 606,452"/>
    <polygon class="accent" points="176,523 211,508 209,546"/>
    <polygon class="accent" points="83,684 163,713 99,769"/>
    <polygon class="accent" points="503,641 542,641 525,676"/>
    <polygon class="accent" points="481,1031 516,1014 513,1053"/>
    <polygon class="accent" points="574,1060 686,1173 686,1200 532,1200"/>

    <polygon points="306,425 610,480 413,720" fill="url(#psych-photo)"
             role="img" aria-label="Portrait photo of guest psychologist Lorena Voss"/>
    <polygon points="116,626 395,560 346,861" fill="url(#goals-photo)"
             role="img" aria-label="Photo of guest speaker Marcus Elwood presenting on stage"/>
  </svg>

  <p class="kicker">December half day Webinar focusing on</p>
  <h1 class="headline">Positive Mindset,<br>Relationships</h1>
  <p class="subhead">and 2021 being a new year<br>with new opportunities</p>

  <div class="speaker speaker--psych">
    <p class="speaker-name"><strong>LORENA</strong> Voss</p>
    <p class="speaker-role">Psychologist</p>
  </div>

  <div class="speaker speaker--goals">
    <p class="speaker-name"><strong>MARCUS</strong> Elwood</p>
    <p class="speaker-role">BucketGoals.com</p>
  </div>

  <p class="event-when">
    <strong>December 10th</strong><br>
    Thursday from<br>
    <strong>12.30pm to 4.30pm</strong> AEST
  </p>

  <p class="pricing">
    Investment $750 + GST per person*
    <small>*enquire for multi booking discounts for 2 people or more</small>
  </p>

  <p class="brand">Tarrow Business Coaching</p>
</main>
</body>
</html>
```